Staff Newsletter Template Image

We are looking for two .jpg images that we can put into a Word document and use for our staff newsletter. We will then add content using text boxes.
Attached is the current template which works for the columns and size that we need but we just want a fresh new design.
The Word document shows how we use it.
The name will stay the same - Team upBeat but can be a different look to the current one.

Target Market(s)

Sales team

Colors

Designer to choose colors to be used in the design.

Requirements
Must have
• Colours will be green, grey and white, possibly cream if needed. All from the guidelines.
• I have attached our brand guidelines which shows design elements and fonts for our brand. Also attached is brand guidelines for one of our product lines as we would like to use the same green.
• It needs to be nice to look at and motivational for our team

```html
<!DOCTYPE html>
<html lang="en">
<head>
<meta charset="utf-8">
<title>Team upBeat – Staff Newsletter</title>
<link href="https://fonts.googleapis.com/css2?family=Carlito:wght@400;700&display=swap" rel="stylesheet">
<style>
  :root {
    --stage: #444444;
    --page-white: #ffffff;
    --sage: #cfe0bf;
    --green: #6a9f45;
    --green-deep: #3f7528;
    --green-text: #3d6a2a;
    --sage-text: #4f7a37;
    --charcoal: #3c3d3c;
    --charcoal-deep: #303130;
    --footer-grey: #a3a6a3;
    --rule-grey: #6a6c6a;
  }
  * { margin: 0; padding: 0; box-sizing: border-box; }
  html, body { width: 1200px; height: 960px; overflow: hidden; background: var(--stage); }
  body { position: relative; font-family: "Carlito", sans-serif; }

  .newsletter-page {
    position: absolute; top: 147px;
    width: 735px; height: 1040px;
    transform: scale(0.64); transform-origin: top left;
    overflow: hidden; background: var(--page-white);
  }
  .page-front { left: 81px; }
  .page-back { left: 636px; }
  .page-shapes { position: absolute; inset: 0; }

  .abs { position: absolute; }
  .issue-date { top: 8px; right: 50px; font-size: 27px; font-weight: 700; color: var(--green-deep); }
  .page-back .issue-date { color: var(--page-white); }
  .masthead { top: 40px; left: 32px; font-size: 50px; font-weight: 700; color: var(--green-deep); }

  .heading { font-weight: 700; font-size: 26px; line-height: 1.2; }
  .body-copy { font-size: 17px; line-height: 20.8px; text-align: justify; }
  .body-copy.end-right { text-align-last: right; }

  .greeting-title { top: 158px; left: 34px; color: var(--page-white); }
  .greeting-copy { top: 188px; left: 34px; width: 325px; color: var(--page-white); }

  .sellers-title { top: 158px; left: 414px; color: var(--green-deep); }
  .sellers-intro { top: 190px; left: 414px; width: 290px; font-size: 17px; line-height: 21px; color: var(--sage-text); }
  .sellers-subtitle { top: 260px; left: 414px; font-size: 21px; font-weight: 700; color: var(--sage-text); }
  .sellers-rule { top: 292px; left: 414px; width: 198px; border-top: 1.5px solid var(--sage-text); }
  .sellers-list { top: 302px; left: 414px; list-style: none; font-size: 17px; line-height: 25px; color: var(--sage-text); }

  .shout-title { top: 604px; left: 34px; color: var(--page-white); }
  .shout-name { top: 600px; left: 160px; width: 268px; height: 40px; border: 1.5px solid var(--page-white); color: var(--page-white); font-size: 26px; font-weight: 700; text-align: center; line-height: 37px; }
  .shout-copy { top: 656px; left: 34px; width: 395px; color: var(--page-white); text-align: left; }

  .tip-title { top: 703px; right: 35px; text-align: right; color: var(--page-white); font-size: 27px; line-height: 33px; }
  .tip-copy { top: 776px; left: 343px; width: 357px; color: var(--page-white); }

  .news-title { top: 124px; left: 34px; color: var(--green-deep); }
  .news-copy { top: 164px; left: 34px; width: 496px; color: var(--green-text); }
  .tips-title { top: 484px; right: 35px; color: var(--green-deep); }
  .tips-copy { top: 520px; left: 29px; width: 671px; color: var(--green-text); }

  .reminders-title { top: 748px; left: 34px; color: var(--page-white); }
  .reminders-copy { top: 785px; left: 34px; width: 322px; color: var(--page-white); }
  .member-title { top: 728px; left: 378px; color: var(--page-white); font-size: 22px; line-height: 26px; }
  .member-copy { top: 785px; left: 378px; width: 322px; color: var(--page-white); }

  .footer-rule { top: 955px; left: 70px; width: 595px; border-top: 1px solid var(--rule-grey); }
  .footer-contacts { top: 966px; left: 0; width: 735px; display: flex; justify-content: center; gap: 40px; font-size: 19px; font-weight: 700; color: var(--footer-grey); }
  .footer-bar { top: 1000px; left: 0; width: 735px; height: 40px; background: var(--charcoal-deep); color: var(--footer-grey); font-size: 15px; text-align: center; line-height: 40px; }
</style>
</head>
<body>

<section class="newsletter-page page-front">
  <svg class="page-shapes" viewBox="0 0 735 1040" width="735" height="1040">
    <defs>
      <linearGradient id="photoTone" x1="0" y1="0" x2="0.4" y2="1">
        <stop offset="0" stop-color="#dfe9d6"/>
        <stop offset="0.45" stop-color="#8fae7b"/>
        <stop offset="1" stop-color="#4a5e40"/>
      </linearGradient>
    </defs>
    <rect width="735" height="1040" fill="var(--charcoal)"/>
    <g role="img" aria-label="Green-toned photo of a hiker with raised arms on a mountain cliff under clouds">
      <rect x="0" y="220" width="735" height="800" fill="url(#photoTone)"/>
    </g>
    <path d="M390,0 L735,0 L735,220 C650,335 540,455 390,520 Z" fill="var(--sage)"/>
    <path d="M0,0 L390,0 L390,520 C300,560 150,585 0,582 Z" fill="var(--green)"/>
    <path d="M0,0 L512,0 C420,90 250,138 0,142 Z" fill="var(--page-white)"/>
    <path d="M0,1040 L0,965 C150,800 300,760 420,722 C600,662 705,560 735,400 L735,1040 Z" fill="var(--charcoal)"/>
    <path d="M0,948 C150,775 300,738 420,700 C600,640 700,520 735,382 L735,400 C705,560 600,662 420,722 C300,760 150,800 0,965 Z" fill="var(--page-white)"/>
  </svg>

  <div class="abs issue-date">12/17/2019</div>
  <div class="abs masthead">Team upBeat</div>

  <h2 class="abs heading greeting-title">Hi Everyone!</h2>
  <p class="abs body-copy greeting-copy">Lorem ipsum dolor sit amet, consectetuer adipiscing elit, sed diam nonummy nibh euismod tincidunt ut laoreet dolore magna aliquam erat volutpat. Ut wisi enim ad minim veniam, quis nostrud exerci tation ullamcorper suscipit lobortis nisl ut aliquip ex ea commodo consequat. Duis autem vel eum iriure dolor in hendrerit in vulputate velit esse molestie consequat, vel illum dolore eu feugiat nulla facilisis at vero eros et accumsan et iusto odio dignissim qui blandit praesent luptatum zzril delenit augue duis dolore te feugait nulla facilisi. aliquip ex ea commodo consequat. Duis autem vel eum iriure dolor in hendrerit in vulputate velit esse molestie consequat, vfacilisi.</p>

  <h2 class="abs heading sellers-title">Top Sellers!</h2>
  <p class="abs sellers-intro">The following upBeat team members were our top sellers last week based on completed sales</p>
  <h3 class="abs sellers-subtitle">Team Member</h3>
  <div class="abs sellers-rule"></div>
  <ul class="abs sellers-list">
    <li>1. -100 upBeat Dollar</li>
    <li>1. -50 upBeat Dollar</li>
    <li>1. -25 upBeat Dollar</li>
    <li>1. -10 upBeat Dollar</li>
    <li>1. -5 upBeat Dollar</li>
  </ul>

  <h2 class="abs heading shout-title">Shout Out</h2>
  <div class="abs shout-name">Name</div>
  <p class="abs body-copy shout-copy">Lorem ipsum dolor sit amet, consectetuer adipiscing elit, sed diam nonummy nibh euismod tincidunt ut laoreet dolore magna aliquam erat volutpat.</p>

  <h2 class="abs heading tip-title">Top Tip from<br>our Week’s Top Seller</h2>
  <p class="abs body-copy end-right tip-copy">Lorem ipsum dolor sit amet, consectetuer adipiscing elit, sed diam nonummy nibh euismod tincidunt ut laoreet dolore magna aliquam erat volutpat. Ut wisi enim ad minim veniam, quis nostrud exerci tation ullamcorper suscipit Ut wisi enim ad minim veniam, quis nostrud exerci tation ullamcorper suscipit lobortisUt</p>

  <div class="abs footer-rule"></div>
  <div class="abs footer-contacts"><span>www.teamupbeat.com.au</span><span>hello@teamupbeat.com.au</span><span>374 555 010 2468</span></div>
  <div class="abs footer-bar">© Copyright 2019 upBeat. All Rights Reserved.</div>
</section>

<section class="newsletter-page page-back">
  <svg class="page-shapes" viewBox="0 0 735 1040" width="735" height="1040">
    <rect width="735" height="1040" fill="var(--page-white)"/>
    <path d="M330,0 L735,0 L735,430 C705,250 580,85 330,0 Z" fill="var(--sage)"/>
    <path d="M0,484 C300,480 560,380 688,250 L694,262 C565,420 300,512 0,515 Z" fill="var(--green)"/>
    <rect x="0" y="708" width="735" height="332" fill="var(--charcoal)"/>
  </svg>

  <div class="abs issue-date">12/17/2019</div>
  <div class="abs masthead">Team upBeat</div>

  <h2 class="abs heading news-title">Company News</h2>
  <p class="abs body-copy news-copy">Lorem ipsum dolor sit amet, consectetuer adipiscing elit, sed diam nonummy nibh euismod tincidunt ut laoreet dolore magna aliquam erat volutpat. Ut wisi enim ad minim veniam, quis nostrud exerci tation ullamcorper suscipit lobortis nisl ut aliquip ex ea commodo consequat. Duis autem vel eum iriure dolor in hendrerit in vulputate velit esse molestie consequat, vel illum dolore eu feugiat nulla facilisis at vero eros et accumsan et iusto odio dignissim qui blandit praesent luptatum zzril delenit augue duis dolore te feugait nulla facilisi. aliquip ex ea commodo consequat. Duis autem vel eum iriure dolor in hendrerit in vulputate velit esse molestie consequat, vfacilisi.</p>

  <h2 class="abs heading tips-title">Tips &amp; Hints</h2>
  <p class="abs body-copy end-right tips-copy">Lorem ipsum dolor sit amet, consectetuer adipiscing elit, sed diam nonummy nibh euismod tincidunt ut laoreet dolore magna aliquam erat volutpat. Ut wisi enim ad minim veniam, quis nostrud exerci tation ullamcorper suscipit lobortis nisl ut aliquip ex ea commodo consequat. Duis autem vel eum iriure dolor in hendrerit in vulputate velit esse molestie consequat, vel illum dolore eu feugiat nulla facilisis at vero eros et accumsan et iusto odio dignissim qui blandit praesent luptatum zzril delenit augue duis dolore te feugait nulla facilisi. aliquip ex ea commodo consequat. Duis autem vel eum iriure dolor in hendrerit in vulputate velit esse molestie consequat, vfacilisi.</p>

  <h2 class="abs heading reminders-title">Reminders</h2>
  <p class="abs body-copy reminders-copy">Lorem ipsum dolor sit amet, consectetuer adipiscing elit, sed diam nonummy nibh euismod tincidunt ut laoreet dolore magna aliquam erat volutpat. Ut wisi enim ad minim veniam, quis nostrud exerci tation ullamcorper suscipit Ut wisi enim ad minim veniam, quis nostrud exerci tation</p>

  <h2 class="abs heading member-title">Being an upBeat Team<br>Member Means…</h2>
  <p class="abs body-copy member-copy">Lorem ipsum dolor sit amet, consectetuer adipiscing elit, sed diam nonummy nibh euismod tincidunt ut laoreet dolore magna aliquam erat volutpat. Ut wisi enim ad minim veniam, quis nostrud exerci tation ullamcorper suscipit Ut wisi enim ad minim veniam, quis nostrud exerci tation</p>

  <div class="abs footer-rule"></div>
  <div class="abs footer-contacts"><span>www.teamupbeat.com.au</span><span>hello@teamupbeat.com.au</span><span>374 555 010 2468</span></div>
  <div class="abs footer-bar">© Copyright 2019 upBeat. All Rights Reserved.</div>
</section>

</body>
</html>
```